IT Company based on Biology Business Needs a Business Card Design

We need a business card design for a new company called 'Lumen CELL'. We develop the machine learning solutions especially focused on deep learning algorithms for biology industry. Our initial product is a vision detection on biological images to help doctors diagnose the symptoms. We would like to see designs that use the color green.

Industry/Entity Type

Business

```html
<!DOCTYPE html>
<html lang="en">
<head>
<meta charset="utf-8">
<title>Lumen CELL — Business Card</title>
<link rel="stylesheet" href="https://fonts.googleapis.com/css2?family=Jost:wght@400;500;600&display=swap">
<style>
  :root {
    --page-bg: #e6e6e4;
    --card-dark: #303134;
    --green-light: #7cc242;
    --green-deep: #1f9a3f;
    --green-text: #78c043;
    --ink-light: #e9e9e9;
    --ink-dark: #2a2b2d;
  }
  * { box-sizing: border-box; margin: 0; padding: 0; }
  html, body { width: 1200px; height: 1000px; overflow: hidden; }
  body {
    background: var(--page-bg);
    font-family: "Jost", sans-serif;
    display: flex; align-items: center; justify-content: center;
  }
  .card {
    position: relative;
    width: 1050px; height: 600px;
    background: var(--card-dark);
    overflow: hidden;
    box-shadow: 0 6px 24px rgba(0,0,0,0.18);
  }
  .card-swoosh { position: absolute; inset: 0; width: 100%; height: 100%; }
  .brand {
    position: absolute; left: 70px; top: 110px;
    display: flex; align-items: center; gap: 18px;
  }
  .brand-dot { width: 46px; height: 46px; border-radius: 50%; background: var(--green-text); }
  .brand-name { font-size: 56px; font-weight: 500; color: var(--green-text); letter-spacing: 1px; line-height: 1; }
  .holder { position: absolute; right: 60px; top: 88px; text-align: right; color: var(--ink-dark); }
  .holder-name { font-size: 34px; font-weight: 600; letter-spacing: 2px; }
  .holder-title { font-size: 24px; font-weight: 400; margin-top: 2px; }
  .contacts { position: absolute; left: 70px; top: 240px; list-style: none; }
  .contacts li {
    display: flex; align-items: center; gap: 18px;
    color: var(--ink-light); font-size: 25px; line-height: 1; margin-bottom: 16px;
  }
  .contact-icon { width: 24px; height: 24px; flex: none; }
  .contact-icon * { fill: none; stroke: var(--green-text); stroke-width: 2; }
  .contact-icon .solid { fill: var(--green-text); stroke: none; }
  .address-block { position: absolute; right: 60px; bottom: 60px; text-align: right; }
  .social-row { display: flex; justify-content: flex-end; gap: 10px; margin-bottom: 20px; }
  .social-dot { width: 36px; height: 36px; border-radius: 50%; background: var(--green-deep); }
  .address { color: var(--ink-light); font-size: 30px; line-height: 1.25; }
</style>
</head>
<body>
  <main class="card">
    <svg class="card-swoosh" viewBox="0 0 1050 600" preserveAspectRatio="none" aria-hidden="true">
      <path d="M0 0 H1050 V300 C820 170 480 30 0 0 Z" fill="var(--green-light)"/>
      <path d="M0 0 C480 30 820 170 1050 300 V330 C820 200 470 50 0 0 Z" fill="var(--green-deep)"/>
    </svg>

    <div class="brand">
      <span class="brand-dot"></span>
      <span class="brand-name">LUMEN CELL</span>
    </div>

    <div class="holder">
      <div class="holder-name">MARA QUILL</div>
      <div class="holder-title">CEO/Founder</div>
    </div>

    <ul class="contacts">
      <li>
        <svg class="contact-icon" viewBox="0 0 24 24"><path d="M6 3 L9 3 L10.5 8 L8.5 9.5 C9.5 12 12 14.5 14.5 15.5 L16 13.5 L21 15 L21 18 C21 19.5 19.5 21 18 21 C10 20.5 3.5 14 3 6 C3 4.5 4.5 3 6 3 Z"/></svg>
        555 204 7731
      </li>
      <li>
        <svg class="contact-icon" viewBox="0 0 24 24"><rect x="7" y="2.5" width="10" height="19" rx="1.5"/><circle class="solid" cx="12" cy="18" r="1.2"/></svg>
        555 318 6402
      </li>
      <li>
        <svg class="contact-icon" viewBox="0 0 24 24"><rect x="2.5" y="5.5" width="19" height="13" rx="1"/><path d="M3 6 L12 13 L21 6"/></svg>
        hello@lumencell.com
      </li>
      <li>
        <svg class="contact-icon" viewBox="0 0 24 24"><circle cx="12" cy="12" r="9.5"/><ellipse cx="12" cy="12" rx="4" ry="9.5"/><path d="M2.5 12 H21.5"/></svg>
        www.lumencell.com
      </li>
    </ul>

    <div class="address-block">
      <div class="social-row" aria-hidden="true">
        <span class="social-dot"></span><span class="social-dot"></span><span class="social-dot"></span>
        <span class="social-dot"></span><span class="social-dot"></span><span class="social-dot"></span>
      </div>
      <p class="address">214 Fernbrook Way<br>Juneau, Alaska 99801</p>
    </div>
  </main>
</body>
</html>
```